Wine label refresh

We are wanting to modify our Corran Estate label to include a picture on it.
I have attached the pictures below which we would like on the label. They are of the Corran Estate vineyard. I have also attached an example of another label with a picture on it that we like the style of.
Industry/Entity Type
Vineyard
Requirements
Must have
- The Corran Estate text must stay the same but can be moved down. It still needs to be the same size though.
Marlborough Sauvignon Blanc should remain in the same font and roughly the same size.
Wine of New Zealand also must stay but could potentially be moved.
Nice to have
- It would be nice if we could keep the KL logo on the front label but feel free to experiment with where this goes.

```html
<!DOCTYPE html>
<html lang="en">
<head>
<meta charset="utf-8">
<title>Corran Estate – Marlborough Sauvignon Blanc 2012</title>
<link rel="stylesheet" href="https://fonts.googleapis.com/css2?family=Cinzel:wght@400&family=Pinyon+Script&family=Lato:wght@300&display=swap">
<style>
  :root {
    --paper: #ffffff;
    --ink: #111111;
    --amber: #d68a0c;
    --cut-line: #2fe3ee;
    --trim-line: #1a1a1a;
    --wine-red: #c8102e;
    --fine-grey: #b0b0ab;
    --sepia-light: #e9dfc4;
    --sepia-mid: #a6946a;
    --sepia-dark: #3e3522;
  }
  html, body {
    margin: 0;
    padding: 0;
    width: 1200px;
    height: 1001px;
    overflow: hidden;
    background: var(--paper);
  }
  .label {
    display: block;
    width: 1200px;
    height: 1001px;
  }
  .brand-name {
    font-family: "Cinzel", "Times New Roman", serif;
    fill: var(--ink);
  }
  .monogram {
    font-family: "Cinzel", "Times New Roman", serif;
    fill: var(--ink);
  }
  .varietal, .vintage {
    font-family: "Pinyon Script", "Snell Roundhand", cursive;
    fill: var(--wine-red);
  }
  .statutory {
    font-family: "Lato", "Gill Sans", sans-serif;
    font-weight: 300;
    fill: var(--fine-grey);
  }
</style>
</head>
<body>
<svg class="label" viewBox="0 0 1200 1001" xmlns="http://www.w3.org/2000/svg">
  <defs>
    <linearGradient id="vineyard-tone" x1="0" y1="0" x2="0" y2="1">
      <stop offset="0" stop-color="var(--sepia-light)"/>
      <stop offset="0.45" stop-color="var(--sepia-mid)"/>
      <stop offset="1" stop-color="var(--sepia-dark)"/>
    </linearGradient>
  </defs>

  <!-- trim and cut guides -->
  <rect class="trim-edge" x="2" y="2" width="1196" height="997" fill="none" stroke="var(--trim-line)" stroke-width="2"/>
  <rect class="cut-line" x="23" y="70" width="1158" height="863" rx="7" fill="none" stroke="var(--cut-line)" stroke-width="2"/>

  <!-- border frames -->
  <rect class="outer-rule" x="46" y="99" width="1111" height="804" fill="none" stroke="var(--amber)" stroke-width="2"/>
  <rect class="border-band" x="70" y="126" width="1063" height="755" fill="var(--amber)"/>
  <rect class="label-field" x="103" y="159" width="998" height="689" fill="var(--paper)"/>
  <rect class="inner-rule" x="115" y="170" width="973" height="666" fill="none" stroke="var(--amber)" stroke-width="2"/>

  <!-- masthead -->
  <text class="monogram" x="150" y="318" font-size="120">KL</text>
  <text class="brand-name" x="395" y="322" font-size="110" textLength="655" lengthAdjust="spacing">Corran Estate</text>

  <!-- vineyard picture area -->
  <rect class="vineyard-photo" x="240" y="349" width="724" height="258" fill="url(#vineyard-tone)"
        role="img" aria-label="Sepia photograph of the Corran Estate vineyard: rows of vines leading to a cottage framed by palm trees, hills behind"/>

  <!-- wine details -->
  <text class="varietal" x="602" y="690" font-size="72" text-anchor="middle" textLength="850" lengthAdjust="spacing">Marlborough Sauvignon Blanc</text>
  <text class="vintage" x="598" y="765" font-size="64" text-anchor="middle">2012</text>

  <g class="statutory" font-size="35">
    <text x="130" y="818">750ml</text>
    <text x="597" y="818" text-anchor="middle">NEW ZEALAND WINE</text>
    <text x="1073" y="818" text-anchor="end">13% alc/vol</text>
  </g>
</svg>
</body>
</html>
```